Healer at the Hearth needs business card

We need a business card that reflects the look and feel of the new website at www.healerathehearth.ca

Our patient navigation and advocacy services are most commonly used by seniors who feel overwhelmed by the health care system and want someone on their side to advocate for their care. Individuals with ill parents or other family members may also come to rely on Healer at the Hearth to help them support their loved one through their health care journey. Ultimately, anyone who finds their health care experience challenging and wants someone completely focused on their needs can benefit from the services of our doctor / nurse team.

Business

Must have
• One design tailored for two clinician which should include: logo, name, title, tel, email, web address and tagline
Nice to have
• A banner image to create a similar look to the website at www.healerathehearth.ca
Should not have
• Too cluttered or busy - must be clean and professional

```html
<!DOCTYPE html>
<html lang="en">
<head>
<meta charset="utf-8">
<title>Healer at the Hearth – Business Card</title>
<link rel="stylesheet" href="https://fonts.googleapis.com/css2?family=Ubuntu:wght@400;500&display=swap">
<style>
  :root {
    --brand-red: #a91d2a;
    --brand-blue: #2f6494;
    --card-white: #fbfbfb;
    --backdrop: #dcdddf;
    --photo-light: #f1f1f1;
    --photo-mid: #d9d9d9;
    --photo-red: #c4202b;
  }
  * { box-sizing: border-box; margin: 0; padding: 0; }
  html, body {
    width: 1200px; height: 900px; overflow: hidden;
    background: var(--backdrop);
    font-family: "Ubuntu", sans-serif;
  }
  .canvas { position: relative; width: 1200px; height: 900px; }
  .card {
    position: absolute; left: 290px;
    width: 620px; height: 354px;
    background: var(--card-white);
    box-shadow: 0 4px 14px rgba(0,0,0,0.18);
    overflow: hidden;
  }
  .card--contact { top: 64px; }
  .card--brand { top: 482px; }

  .stripes { position: absolute; left: 0; right: 0; }
  .stripes__red { height: 16px; background: var(--brand-red); }
  .stripes__gap { height: 3px; background: var(--card-white); }
  .stripes__blue { height: 12px; background: var(--brand-blue); }

  /* contact card */
  .brand-mini {
    position: absolute; left: 26px; top: 22px;
    display: flex; align-items: center; gap: 10px;
  }
  .brand-mini__dot { width: 40px; height: 40px; border-radius: 50%; background: var(--brand-red); }
  .brand-mini__name {
    color: var(--brand-blue); font-size: 24px; line-height: 1.0; font-weight: 400;
    width: 130px;
  }
  .banner-photo {
    position: absolute; left: 0; right: 0; top: 112px; height: 178px;
    background: linear-gradient(90deg, var(--photo-light) 0%, var(--photo-light) 38%, var(--photo-mid) 48%, var(--photo-red) 62%, #e8e8e8 78%, var(--photo-light) 100%);
  }
  .contact-list {
    position: absolute; left: 28px; top: 200px;
    list-style: none; font-size: 13px; line-height: 21px;
  }
  .contact-list__label { color: var(--brand-red); }
  .contact-list__value { color: var(--brand-blue); }
  .clinician {
    position: absolute; right: 36px; top: 86px; text-align: right;
  }
  .clinician__name { color: var(--brand-red); font-size: 16px; font-weight: 500; }
  .clinician__title { color: var(--brand-blue); font-size: 10px; margin-top: 4px; }
  .card--contact .stripes { top: 292px; }

  /* brand card */
  .brand-lockup {
    position: absolute; left: 104px; top: 96px;
    display: flex; align-items: center; gap: 22px;
  }
  .brand-lockup__dot { width: 124px; height: 124px; border-radius: 50%; background: var(--brand-red); }
  .brand-lockup__name {
    color: var(--brand-blue); font-size: 44px; line-height: 1.0; font-weight: 400;
    width: 260px;
  }
  .card--brand .stripes { top: 290px; }
</style>
</head>
<body>
<main class="canvas">

  <section class="card card--contact">
    <div class="banner-photo" role="img" aria-label="Photo of a clinician in a white coat holding a red heart"></div>
    <div class="brand-mini">
      <span class="brand-mini__dot"></span>
      <span class="brand-mini__name">Healer at the Hearth</span>
    </div>
    <div class="clinician">
      <p class="clinician__name">Employee Name</p>
      <p class="clinician__title">Title</p>
    </div>
    <ul class="contact-list">
      <li><span class="contact-list__label">Phone:</span><span class="contact-list__value">555-014-2236</span></li>
      <li><span class="contact-list__label">Email:</span> <span class="contact-list__value">info@healerathehearth.ca</span></li>
      <li><span class="contact-list__label">Web:</span> <span class="contact-list__value">www.healerathehearth.ca</span></li>
    </ul>
    <div class="stripes">
      <div class="stripes__red"></div>
      <div class="stripes__gap"></div>
      <div class="stripes__blue"></div>
    </div>
  </section>

  <section class="card card--brand">
    <div class="brand-lockup">
      <span class="brand-lockup__dot"></span>
      <span class="brand-lockup__name">Healer at the Hearth</span>
    </div>
    <div class="stripes">
      <div class="stripes__red"></div>
      <div class="stripes__gap"></div>
      <div class="stripes__blue"></div>
    </div>
  </section>

</main>
</body>
</html>
```